Stationery design bilingual preschool
Meadowlark preschool
Stationery design bilingual preschool - Childcare
Creative Brief
Bright & Fun-filled
Marita Sundqvist
Preschool director
Lövhagsvägen 9 128 31 Skarpnäck Sweden
angsfagelforskolan@postlada.se
www.angsfagelforskolan.com
Back of the business card suppose to have the same information as the front side but on Swedish.
(Subtitle) Ängsfågel Förskola AB ( name) Marita Sundqvist (title) Förskolechef (address) Lövhagsvägen 9 128 31 Skarpnäck (phone) Tel. 08 731 94 62 (cell) Mob. 073 862 40 15 (email) angsfagelforskolan@postlada.com (web side) www.angsfagelforskolan. com
butterfly2004 butterfly2004
Dear designers, I'd like to see design drafts ideas for the following products: 1. Business card 2. Letterhead 3. Envelope 4. Folder 5. CD and CD cover 6. Email signature 7. Presentation 8.Thank you card 8. Stamp 9. T-shirt, Hoody, Winter jacket/ Rain jacket, Cap, Scarf 10. Pen 11. Meadowlark character toy Thank you, PH

```html
<!DOCTYPE html>
<html lang="en">
<head>
<meta charset="utf-8">
<title>Meadowlark preschool – Business card</title>
<link rel="stylesheet" href="https://fonts.googleapis.com/css2?family=Open+Sans:wght@400;600;800&display=swap">
<style>
  :root {
    --page-bg: #e4e4e6;
    --card-bg: #ffffff;
    --brand-green: #6fb52c;
    --brand-orange: #f08a1c;
    --brand-purple: #8a2f9a;
    --brand-yellow: #f7c21b;
    --text-grey: #5a5a5a;
    --text-light: #9a9a9a;
    --rule: #cfcfcf;
  }
  * { box-sizing: border-box; margin: 0; padding: 0; }
  html, body {
    width: 1200px;
    height: 871px;
    overflow: hidden;
    background: var(--page-bg);
    font-family: "Open Sans", Arial, sans-serif;
  }
  .card {
    position: absolute;
    top: 270px;
    width: 540px;
    height: 320px;
    background: var(--card-bg);
    border-radius: 18px;
    overflow: hidden;
    box-shadow: 0 12px 28px rgba(0,0,0,0.16);
  }
  .card-back { left: 40px; }
  .card-front { left: 620px; }

  /* Back */
  .back-brand {
    position: absolute;
    left: 0;
    right: 0;
    top: 92px;
    display: flex;
    justify-content: center;
    align-items: center;
    gap: 12px;
  }
  .brand-dot {
    width: 22px;
    height: 22px;
    border-radius: 50%;
    background: var(--brand-orange);
    flex: none;
  }
  .back-brand .brand-name {
    font-weight: 800;
    font-size: 38px;
    line-height: 1;
    color: var(--brand-green);
  }
  .back-subtitle {
    position: absolute;
    left: 0;
    right: 0;
    top: 144px;
    text-align: center;
    font-size: 13px;
    font-weight: 600;
    color: var(--brand-purple);
  }
  .back-rule {
    position: absolute;
    left: 120px;
    right: 120px;
    top: 196px;
    border-top: 1px solid var(--rule);
  }
  .back-web {
    position: absolute;
    left: 0;
    right: 0;
    top: 206px;
    text-align: center;
    font-size: 12px;
    color: var(--text-light);
    letter-spacing: 0.5px;
  }

  /* Front */
  .front-brand {
    position: absolute;
    left: 30px;
    top: 26px;
    font-weight: 800;
    font-size: 34px;
    line-height: 1;
    color: var(--brand-green);
  }
  .contact {
    position: absolute;
    left: 30px;
    top: 118px;
    width: 250px;
  }
  .contact-name {
    font-weight: 600;
    font-size: 17px;
    color: var(--brand-orange);
  }
  .contact-title {
    font-size: 11px;
    color: var(--brand-green);
  }
  .contact-address {
    margin-top: 12px;
    font-size: 11px;
    line-height: 1.5;
    color: var(--text-grey);
  }
  .contact-lines {
    margin-top: 10px;
    list-style: none;
  }
  .contact-lines li {
    display: flex;
    align-items: center;
    gap: 8px;
    font-size: 11px;
    line-height: 1.75;
    color: var(--text-grey);
  }
  .contact-lines svg {
    width: 12px;
    height: 12px;
    flex: none;
    fill: var(--brand-green);
  }
  .mascot-area {
    position: absolute;
    left: 290px;
    top: 62px;
    width: 250px;
    height: 258px;
    border-top-left-radius: 40px;
    background: linear-gradient(150deg, #9bd04a 0%, #a04db0 55%, var(--brand-orange) 100%);
  }
</style>
</head>
<body>
  <section class="card card-back">
    <div class="back-brand">
      <span class="brand-dot"></span>
      <span class="brand-name">Meadowlark preschool</span>
    </div>
    <p class="back-subtitle">Ängsfågel Förskola AB</p>
    <div class="back-rule"></div>
    <p class="back-web">www.angsfagelforskolan.com</p>
  </section>

  <section class="card card-front">
    <h1 class="front-brand">Meadowlark<br>preschool</h1>

    <div class="contact">
      <p class="contact-name">Marita Sundqvist</p>
      <p class="contact-title">Preschool director</p>
      <p class="contact-address">Lövhagsvägen 9<br>128 31 Skarpnäck, Sweden</p>
      <ul class="contact-lines">
        <li>
          <svg viewBox="0 0 24 24" aria-hidden="true"><path d="M6.6 10.8a15.1 15.1 0 0 0 6.6 6.6l2.2-2.2c.3-.3.7-.4 1-.2 1.1.4 2.3.6 3.6.6.6 0 1 .4 1 1V20c0 .6-.4 1-1 1A17 17 0 0 1 3 4c0-.6.4-1 1-1h3.5c.6 0 1 .4 1 1 0 1.3.2 2.5.6 3.6.1.3 0 .7-.2 1z"/></svg>
          +46 8 731 94 62
        </li>
        <li>
          <svg viewBox="0 0 24 24" aria-hidden="true"><path d="M7 2h10a2 2 0 0 1 2 2v16a2 2 0 0 1-2 2H7a2 2 0 0 1-2-2V4a2 2 0 0 1 2-2zm0 3v13h10V5zm5 14.2a1 1 0 1 0 0 2 1 1 0 0 0 0-2z"/></svg>
          +46 73 862 40 15
        </li>
        <li>
          <svg viewBox="0 0 24 24" aria-hidden="true"><path d="M3 5h18a1 1 0 0 1 1 1v12a1 1 0 0 1-1 1H3a1 1 0 0 1-1-1V6a1 1 0 0 1 1-1zm9 7.5L4 7.2V17h16V7.2z"/></svg>
          angsfagelforskolan@postlada.se
        </li>
      </ul>
    </div>

    <div class="mascot-area" role="img" aria-label="Meadowlark character toy illustration"></div>
  </section>
</body>
</html>
```